New Company Business Card Design

I have a new company logo and I want a new business card design. I dont know if the logo file i attached is in the correct format or quality. We are a New York City Specialty construction Firm specializing in high risk out of the box projects. I want a simple and classy business card that people will his card is as crisp as the work his company does.

Target Market(s)

Clients in the heavy construction industry in New York City

Industry/Entity Type

Construction Company

Contact Information for Business Card

Simple Classy - DIFFERENT

Font styles to use
Other font styles liked:
• Mach the logo font in some way

Colors

Designer to choose colors to be used in the design.

Requirements
Must have
• Uniqueness
Nice to have
• Nothing particular - Just different and classy - Timeless
Should not have
• Goofy Shit or Gimmicky shit

```html
<!DOCTYPE html>
<html lang="en">
<head>
<meta charset="utf-8">
<title>Kestrel Build Group – Business Card</title>
<link rel="stylesheet" href="https://fonts.googleapis.com/css2?family=Fira+Sans:wght@400;600;800&display=swap">
<style>
  :root {
    --backdrop: #e9e9e9;
    --card: #ffffff;
    --brand-blue: #1c63a8;
    --ink: #3a3a3a;
    --rule: #8fb0d4;
  }
  * { margin: 0; padding: 0; box-sizing: border-box; }
  html, body {
    width: 1200px; height: 1200px; overflow: hidden;
    background: var(--backdrop);
    font-family: "Fira Sans", Arial, sans-serif;
  }
  .canvas {
    position: relative; width: 1200px; height: 1200px;
    display: flex; justify-content: center; align-items: center; gap: 100px;
  }
  .card {
    position: relative; width: 400px; height: 700px;
    background: var(--card);
    box-shadow: 0 2px 10px rgba(0,0,0,0.08);
  }
  /* Front side */
  .card-front .identity { position: absolute; left: 50px; top: 90px; }
  .identity .person-name {
    color: var(--brand-blue); font-weight: 600; font-size: 30px; letter-spacing: 0.5px;
  }
  .identity .person-role { color: var(--ink); font-size: 16px; margin-top: 4px; margin-left: 8px; }

  .contact { position: absolute; left: 52px; bottom: 90px; color: var(--ink); font-size: 17px; }
  .contact svg { width: 16px; height: 16px; flex: none; color: var(--brand-blue); fill: currentColor; }

  .contact-group { position: relative; padding-left: 28px; }
  .contact-group.address .pin { position: absolute; left: -8px; top: 4px; }
  .contact-group.address::after {
    content: ""; position: absolute; left: 0; top: 30px; height: 46px;
    border-left: 1.5px solid var(--rule);
  }
  .address-lines span { display: block; line-height: 24px; }
  .address-lines span + span { padding-left: 12px; }

  .contact-group.digital { margin-top: 12px; }
  .contact-group.digital::before {
    content: ""; position: absolute; left: 0; top: 26px; bottom: -4px;
    border-left: 1.5px solid var(--rule);
  }
  .contact-row { display: flex; align-items: center; gap: 12px; line-height: 26px; }
  .contact-row + .contact-row { margin-left: 14px; }

  /* Back side */
  .card-back { display: flex; justify-content: center; align-items: center; }
  .brand-mark { display: flex; align-items: center; gap: 12px; }
  .brand-mark .brand-square { width: 22px; height: 22px; background: var(--brand-blue); }
  .brand-mark .brand-name {
    color: var(--brand-blue); font-weight: 800; font-size: 30px; letter-spacing: 1px;
    text-transform: uppercase;
  }
</style>
</head>
<body>
<main class="canvas">
  <section class="card card-front" aria-label="Business card front">
    <div class="identity">
      <h1 class="person-name">JOHN DOE</h1>
      <p class="person-role">Director</p>
    </div>
    <div class="contact">
      <div class="contact-group address">
        <svg class="pin" viewBox="0 0 16 16" aria-hidden="true"><path d="M8 0a5.5 5.5 0 0 0-5.5 5.5C2.5 10 8 16 8 16s5.5-6 5.5-10.5A5.5 5.5 0 0 0 8 0zm0 8a2.5 2.5 0 1 1 0-5 2.5 2.5 0 0 1 0 5z"/></svg>
        <div class="address-lines"><span>Dummy city</span><span>Dummy Country Land</span></div>
      </div>
      <div class="contact-group digital">
        <div class="contact-row">
          <svg viewBox="0 0 16 16" aria-hidden="true"><path d="M2 4c0-1 1-2 6-2s6 1 6 2l-1.5 2c-1-.5-2-.7-2.5-.5L9.5 7h-3L6 5.5C5.5 5.3 4.5 5.5 3.5 6zM3 9l2-2h6l2 2v5H3zm5 1.2a1.3 1.3 0 1 0 0 2.6 1.3 1.3 0 0 0 0-2.6z"/></svg>
          <span>1-234-567890</span>
        </div>
        <div class="contact-row">
          <svg viewBox="0 0 16 16" aria-hidden="true"><path d="M1 3h14v10H1zm1.5 1.3v.4L8 8.6l5.5-3.9v-.4zm0 2.2v5.2h11V6.5L8 10.4z"/></svg>
          <span>john@kestrelbuild.com</span>
        </div>
        <div class="contact-row">
          <svg viewBox="0 0 16 16" aria-hidden="true"><g fill="none" stroke="currentColor" stroke-width="1.4"><circle cx="8" cy="8" r="6.3"/><ellipse cx="8" cy="8" rx="2.8" ry="6.3"/><path d="M1.7 8h12.6"/></g></svg>
          <span>www.kestrelbuild.com</span>
        </div>
      </div>
    </div>
  </section>
  <section class="card card-back" aria-label="Business card back">
    <div class="brand-mark">
      <span class="brand-square" aria-hidden="true"></span>
      <span class="brand-name">Kestrel Build</span>
    </div>
  </section>
</main>
</body>
</html>
```